Occupational Therapy Clinic Advertisement

Create an advertisement for a magazine. Below I have attached my original ad (Ad 2020.pdf) . I want the ad changed and it should be eye catching. I would like a eye catching graphics added in the ad. It should be a graphic image that applies to education. I am attaching a sample graphic image of that I liked from someone elses ad- it should not be the same- it just is there to show what I like. Please use the same words from my original ad.Dimensions: 3.75in x 10.3 in

Target Market(s)

Parents of School aged children

Requirements
Must have
• Must have eye catching Graphic. Colors should be eye catching for a typed magazine.

```html
<!DOCTYPE html>
<html lang="en">
<head>
<meta charset="utf-8">
<title>Bright Steps OT Services</title>
<link rel="stylesheet" href="https://fonts.googleapis.com/css2?family=Archivo+Black&family=Arimo:wght@400;700&family=Fira+Sans+Condensed:wght@500&family=Fira+Sans+Extra+Condensed:wght@500;700&family=Lobster&display=swap">
<style>
:root{
  --navy:#033a78;
  --red:#e4003f;
  --teal:#0096b0;
  --green:#52ae32;
  --yellow:#ffee00;
  --sky:#dcf0fc;
  --ink:#1a1a1a;
  --white:#ffffff;
}
*{margin:0;padding:0;box-sizing:border-box}
html,body{width:1200px;height:3293px;overflow:hidden}
body{position:relative;background:var(--sky);font-family:"Fira Sans Condensed",sans-serif}
.abs{position:absolute;left:0;width:1200px;text-align:center}
.header{position:absolute;top:0;left:0;width:1200px;height:348px;background:var(--navy)}
.brand-name{top:70px;font-family:"Fira Sans Extra Condensed",sans-serif;font-weight:700;font-size:118px;line-height:130px;color:var(--white)}
.brand-phone{top:232px;font-family:"Arimo",sans-serif;font-weight:700;font-size:72px;line-height:80px;color:var(--white)}
.tricolor{position:absolute;top:348px;left:0;width:1200px;height:6px;display:flex}
.tricolor span{flex:1}
.graphic{position:absolute;top:0;left:0}
.bubble-text{position:absolute;text-align:center;font-family:"Fira Sans Extra Condensed",sans-serif;font-weight:500;font-size:58px;line-height:59px;color:var(--white)}
.band-text{position:absolute;left:0;width:1200px;text-align:center;font-family:"Fira Sans Extra Condensed",sans-serif;font-weight:700;font-size:62px;color:var(--white)}
.band-copy{font-family:"Fira Sans Extra Condensed",sans-serif;font-size:64px;line-height:70px;color:var(--ink);font-weight:500}
.ages{font-family:"Arimo",sans-serif;font-size:60px;line-height:70px;color:var(--ink)}
.tagline{font-family:"Lobster",cursive;font-size:64px;line-height:80px;color:var(--red)}
.footer{position:absolute;top:2699px;left:0;width:1200px;height:594px;background:var(--navy)}
.accepted{font-family:"Fira Sans Extra Condensed",sans-serif;font-weight:700;font-size:70px;line-height:76px;color:var(--yellow)}
.info{font-family:"Fira Sans Extra Condensed",sans-serif;font-size:48px;line-height:60px;color:var(--white);font-weight:500}
.info .mail{color:var(--yellow)}
.therapist{font-family:"Fira Sans Extra Condensed",sans-serif;font-weight:700;font-size:62px;line-height:70px;color:var(--yellow)}
.footer-phone{font-family:"Fira Sans Extra Condensed",sans-serif;font-size:58px;line-height:66px;color:var(--white);font-weight:500}
</style>
</head>
<body>

<header class="header">
  <div class="abs brand-name">Bright Steps OT Services</div>
  <div class="abs brand-phone">(718) 555 - 0142</div>
</header>
<div class="tricolor"><span style="background:var(--red)"></span><span style="background:var(--teal)"></span><span style="background:var(--green)"></span></div>

<svg class="graphic" width="1200" height="2699" viewBox="0 0 1200 2699">
  <g fill="none" stroke="#1a1a1a" stroke-width="3">
    <polyline points="543,383 543,458 256,458 256,884"/>
    <line x1="599" y1="383" x2="599" y2="550"/>
    <polyline points="656,383 656,458 943,458 943,884"/>
    <circle cx="599" cy="769" r="220"/>
    <circle cx="256" cy="1104" r="220"/>
    <circle cx="943" cy="1104" r="220"/>
  </g>
  <g fill="none" stroke-width="10">
    <circle cx="599" cy="769" r="220" stroke="var(--teal)" stroke-dasharray="560 1400" transform="rotate(70 599 769)"/>
    <circle cx="256" cy="1104" r="220" stroke="var(--red)" stroke-dasharray="560 1400" transform="rotate(70 256 1104)"/>
    <circle cx="943" cy="1104" r="220" stroke="var(--green)" stroke-dasharray="560 1400" transform="rotate(70 943 1104)"/>
  </g>
  <circle cx="599" cy="769" r="195" fill="var(--teal)"/>
  <circle cx="256" cy="1104" r="195" fill="var(--red)"/>
  <circle cx="943" cy="1104" r="195" fill="var(--green)"/>
  <circle cx="543" cy="383" r="15" fill="var(--red)"/>
  <circle cx="599" cy="383" r="15" fill="var(--teal)"/>
  <circle cx="656" cy="383" r="15" fill="var(--green)"/>

  <text x="600" y="1502" text-anchor="middle" font-family="Fira Sans Extra Condensed, sans-serif" font-weight="700" font-size="150" fill="var(--navy)" textLength="857" lengthAdjust="spacingAndGlyphs">YES YOUR CHILD</text>
  <text x="600" y="1904" text-anchor="middle" font-family="Archivo Black, sans-serif" font-size="520" fill="var(--navy)" textLength="857" lengthAdjust="spacingAndGlyphs">CAN</text>
  <line x1="236" y1="1562" x2="1010" y2="1888" stroke="var(--red)" stroke-width="13"/>
  <text x="600" y="2006" text-anchor="middle" font-family="Fira Sans Extra Condensed, sans-serif" font-weight="700" font-size="100" fill="var(--navy)" textLength="857" lengthAdjust="spacingAndGlyphs">Will Succeed in School!</text>

  <g fill="var(--red)">
    <polygon points="0,2055 360,2055 388,2092 360,2128 0,2128"/>
    <polygon points="370,2055 832,2055 806,2092 832,2128 370,2128 398,2092"/>
    <polygon points="850,2055 1200,2055 1200,2128 850,2128 824,2092"/>
  </g>
  <g fill="var(--teal)">
    <polygon points="0,2245 397,2245 424,2282 397,2319 0,2319"/>
    <polygon points="407,2245 792,2245 766,2282 792,2319 407,2319 434,2282"/>
    <polygon points="810,2245 1200,2245 1200,2319 810,2319 784,2282"/>
  </g>
  <g fill="var(--green)">
    <polygon points="0,2436 442,2436 469,2473 442,2511 0,2511"/>
    <polygon points="452,2436 741,2436 715,2473 741,2511 452,2511 479,2473"/>
    <polygon points="759,2436 1200,2436 1200,2511 759,2511 733,2473"/>
  </g>
</svg>

<div class="bubble-text" style="left:449px;width:300px;top:650px">Knows the information but fails the test?</div>
<div class="bubble-text" style="left:86px;width:340px;top:985px">Does your child struggle with Reading/ Kriah?</div>
<div class="bubble-text" style="left:773px;width:340px;top:985px">Has difficulty remembering names and dates?</div>

<div class="band-text" style="top:2053px;line-height:78px">WE EVALUATE:</div>
<div class="abs band-copy" style="top:2133px">Using standardized Evaluations</div>
<div class="band-text" style="top:2243px;line-height:78px">WE TREAT:</div>
<div class="abs band-copy" style="top:2323px">Using Researched based techniques</div>
<div class="band-text" style="top:2434px;line-height:78px">AGES:</div>
<div class="abs ages" style="top:2517px">6-18</div>
<div class="abs tagline" style="top:2597px">We Treat the underlying processing deficits</div>

<footer class="footer">
  <div class="abs accepted" style="top:20px">Board of Ed OT RSA's accepted</div>
  <div class="abs info" style="top:111px">Located in Borough Park<br>Evaluations done in Borough Park &amp; Staten Island</div>
  <div class="abs info" style="top:261px">For more information or to be added to our email list,<br>please email: <span class="mail">brightstepsot@example.com</span></div>
  <div class="abs therapist" style="top:412px">Miriam Adler OTR/L</div>
  <div class="abs footer-phone" style="top:489px">(718) 555 - 0142</div>
</footer>

</body>
</html>
```